Business cards and logo for a international shipping company called Meridane Freight LLC. We would like to incorporate the colors red and blue. We would like the theme to be nautical.

Industry/Entity Type

Business

```html
<!DOCTYPE html>
<html lang="en">
<head>
<meta charset="utf-8">
<title>Meridane Freight LLC — Business Cards</title>
<link href="https://fonts.googleapis.com/css2?family=Source+Sans+3:wght@400;600&display=swap" rel="stylesheet">
<style>
  :root {
    --backdrop: #2a2a2c;
    --card-top: #1b212b;
    --card-bottom: #2b323d;
    --brand-blue: #3a78c4;
    --brand-red: #d8322f;
    --text-light: #c9ced6;
    --text-muted: #9aa3af;
  }
  * { margin: 0; padding: 0; box-sizing: border-box; }
  html, body {
    width: 1200px; height: 716px; overflow: hidden;
    background: var(--backdrop);
    font-family: "Source Sans 3", sans-serif;
  }
  .stage {
    width: 1200px; height: 716px;
    display: flex; align-items: center; justify-content: center; gap: 48px;
  }
  .card {
    width: 525px; height: 300px;
    background: linear-gradient(160deg, var(--card-top), var(--card-bottom));
    border-radius: 4px;
    box-shadow: 0 12px 30px rgba(0,0,0,0.45);
    position: relative;
    display: flex; align-items: center;
  }
  .card-front { justify-content: center; }
  .brand {
    display: flex; align-items: center; gap: 10px;
  }
  .brand-mark {
    width: 16px; height: 16px; background: var(--brand-red);
  }
  .brand-name {
    font-weight: 600; color: var(--brand-blue);
    font-size: 34px; letter-spacing: 0.5px; line-height: 1;
  }
  .card-back .brand-name { font-size: 24px; }
  .card-back .brand { position: absolute; left: 40px; top: 50%; transform: translateY(-50%); }
  .divider {
    position: absolute; left: 262px; top: 40px; bottom: 40px;
    width: 2px; background: var(--brand-red);
  }
  .contact {
    position: absolute; left: 290px; top: 58px;
    color: var(--text-light);
  }
  .person-name { font-size: 24px; line-height: 1; }
  .job-title { font-size: 13px; color: var(--brand-red); margin: 4px 0 14px; }
  .contact-list { list-style: none; }
  .contact-list li {
    display: flex; align-items: center; gap: 8px;
    font-size: 15px; line-height: 24px;
  }
  .contact-list svg { width: 14px; height: 14px; fill: var(--brand-blue); flex: none; }
  .social-mark { width: 12px; height: 12px; background: var(--brand-red); flex: none; margin-right: 2px; }
</style>
</head>
<body>
<main class="stage">
  <section class="card card-front">
    <div class="brand">
      <span class="brand-mark"></span>
      <span class="brand-name">Meridane Freight</span>
    </div>
  </section>

  <section class="card card-back">
    <div class="brand">
      <span class="brand-mark"></span>
      <span class="brand-name">Meridane Freight</span>
    </div>
    <div class="divider"></div>
    <div class="contact">
      <p class="person-name">Your Name</p>
      <p class="job-title">Job Title</p>
      <ul class="contact-list">
        <li>
          <svg viewBox="0 0 16 16"><path d="M1 3h14v10H1z M1 3l7 6 7-6" stroke="#1b212b" stroke-width="1"/></svg>
          youremail@meridane.co
        </li>
        <li>
          <svg viewBox="0 0 16 16"><path d="M1 6c0-3 14-3 14 0v2h-4V6H5v2H1z M3 9h10l1 5H2z"/></svg>
          000 000 0000
        </li>
        <li>
          <svg viewBox="0 0 16 16"><path d="M4 1h8v14H4z M5 3v9h6V3z" fill-rule="evenodd"/></svg>
          000 000 0000
        </li>
        <li>
          <svg viewBox="0 0 16 16"><path d="M8 1a5 5 0 0 1 5 5c0 4-5 9-5 9S3 10 3 6a5 5 0 0 1 5-5zm0 3a2 2 0 1 0 0 4 2 2 0 0 0 0-4z" fill-rule="evenodd"/></svg>
          your address
        </li>
        <li>
          <span class="social-mark"></span>
          /meridanefreight
        </li>
      </ul>
    </div>
  </section>
</main>
</body>
</html>
```